Best in class business looking for best in class stationery that accurately reflects the brand image we are trying to build as the brand expands throughout the country. The Varying items should be an eye catching design that makes even the simplest letter or small business card stand out in the crowd.

Target Market(s)

Professionals

Industry/Entity Type

Real Estate

Other font styles liked:
• See atttached logo

Requirements
Must have
• Letterhead
• Business cards
• Envelopes
• Labels for larger mailings
Nice to have
• Folders
• Notebook
Should not have
• Stale design elements

```html
<!DOCTYPE html>
<html lang="en">
<head>
<meta charset="utf-8">
<title>Summit Vale Management Corporation — Stationery</title>
<link rel="stylesheet" href="https://fonts.googleapis.com/css2?family=Open+Sans:wght@400;600;700&display=swap">
<style>
  :root {
    --navy: #1f2f86;
    --royal: #2b40a3;
    --bright: #4a66c8;
    --pale: #e4e8f3;
    --white: #ffffff;
    --ink: #27348f;
    --bg-light: #ecebe8;
    --bg-dark: #1c1c1e;
    --bg-white: #ffffff;
    --bg-grey: #e9e9ea;
  }
  * { box-sizing: border-box; margin: 0; padding: 0; }
  html, body { width: 1200px; height: 2571px; overflow: hidden; }
  body { position: relative; font-family: "Open Sans", Arial, sans-serif; color: var(--ink); }

  .band { position: absolute; left: 0; width: 1200px; }
  .band--stationery { top: 0; height: 900px; background: var(--bg-light); }
  .band--cards { top: 900px; height: 860px; background: var(--bg-dark); }
  .band--label { top: 1760px; height: 811px; left: 0; width: 600px; background: var(--bg-white); }
  .band--notebook { top: 1760px; height: 811px; left: 600px; width: 600px; background: var(--bg-grey); }

  .piece { position: absolute; overflow: hidden; box-shadow: 0 6px 18px rgba(0,0,0,.18); }
  .piece--white { background: var(--white); }
  .piece--blue { background: linear-gradient(135deg, var(--royal), var(--navy)); }

  .wave { position: absolute; left: 0; bottom: 0; width: 100%; }

  .lockup { position: absolute; display: flex; align-items: center; gap: 6px; font-weight: 600; color: var(--navy); letter-spacing: .04em; text-transform: uppercase; line-height: 1.15; }
  .lockup__mark { flex: none; background: currentColor; }
  .lockup--light { color: var(--white); }

  .faint-block { position: absolute; background: var(--pale); opacity: .8; }
  .piece--blue .faint-block { background: var(--white); opacity: .07; }

  .footer-text { position: absolute; color: var(--white); font-size: 8px; text-align: right; line-height: 1.5; }

  .contact-list { position: absolute; list-style: none; color: var(--ink); }
  .contact-list li { display: flex; align-items: center; gap: 8px; }
  .contact-list svg { flex: none; fill: var(--ink); }

  .person__name { position: absolute; font-weight: 600; color: var(--royal); }
  .person__role { position: absolute; color: var(--royal); }

  .label__line { position: absolute; height: 1px; background: var(--bright); }
  .label__band { position: absolute; left: 0; bottom: 0; width: 100%; background: var(--navy); }

  .spiral { position: absolute; left: -14px; top: 30px; display: flex; flex-direction: column; gap: 17.5px; }
  .spiral span { display: block; width: 30px; height: 14px; border: 3px solid #c8c8cc; border-radius: 8px; }
</style>
</head>
<body>

<!-- Stationery set -->
<section class="band band--stationery">

  <!-- Envelope (top) -->
  <div class="piece piece--white envelope" style="left:60px;top:60px;width:560px;height:270px;">
    <div style="position:absolute;left:0;top:0;width:100%;height:22px;background:var(--navy);"></div>
    <div class="faint-block" style="left:40px;top:110px;width:110px;height:110px;"></div>
    <div class="lockup" style="left:40px;top:40px;font-size:12px;"><span class="lockup__mark" style="width:12px;height:12px;"></span>Summit Vale Management Corporation</div>
    <div style="position:absolute;left:0;bottom:0;width:100%;height:6px;background:var(--navy);"></div>
  </div>

  <!-- Business card front (blue) -->
  <div class="piece piece--blue card-small" style="left:60px;top:370px;width:260px;height:150px;">
    <div class="faint-block" style="left:120px;top:50px;width:90px;height:90px;"></div>
    <div class="lockup lockup--light" style="left:22px;top:60px;width:220px;font-size:10px;"><span class="lockup__mark" style="width:10px;height:10px;"></span>Summit Vale Management Corporation</div>
  </div>

  <!-- Business card back (white) -->
  <div class="piece piece--white card-small" style="left:340px;top:370px;width:260px;height:150px;">
    <div class="lockup" style="left:120px;top:18px;width:130px;font-size:7px;"><span class="lockup__mark" style="width:8px;height:8px;"></span>Summit Vale Management Corporation</div>
    <div style="position:absolute;left:20px;top:20px;font-size:10px;font-weight:600;color:var(--royal);">Alan Porter</div>
    <div style="position:absolute;left:20px;top:34px;font-size:7px;color:var(--royal);">Manager</div>
    <div style="position:absolute;left:20px;top:54px;font-size:6px;line-height:1.6;color:var(--ink);">18 Harbor Lane, Suite 300<br>Easton, MA 02375<br>555-014-2200<br>info@summitvale.com</div>
    <svg class="wave" viewBox="0 0 260 50" height="50" preserveAspectRatio="none" aria-hidden="true">
      <path d="M0 22 C70 4 150 40 260 10 L260 50 L0 50 Z" fill="var(--bright)"/>
      <path d="M0 30 C80 14 160 46 260 20 L260 50 L0 50 Z" fill="var(--navy)"/>
    </svg>
  </div>

  <!-- Envelope with wave -->
  <div class="piece piece--white envelope" style="left:60px;top:560px;width:560px;height:290px;">
    <div class="lockup" style="left:30px;top:28px;width:220px;font-size:11px;"><span class="lockup__mark" style="width:11px;height:11px;"></span>Summit Vale Management Corporation</div>
    <div class="faint-block" style="left:30px;top:110px;width:120px;height:110px;"></div>
    <svg class="wave" viewBox="0 0 560 110" height="110" preserveAspectRatio="none" aria-hidden="true">
      <path d="M0 70 C160 30 330 100 560 20 L560 110 L0 110 Z" fill="var(--bright)"/>
      <path d="M0 82 C170 46 340 112 560 34" fill="none" stroke="#fff" stroke-width="3"/>
      <path d="M0 92 C180 60 350 118 560 48 L560 110 L0 110 Z" fill="var(--navy)"/>
    </svg>
    <p class="footer-text" style="right:22px;bottom:14px;">If undeliverable please return to:<br>18 Harbor Lane, Suite 300<br>Easton, MA 02375</p>
  </div>

  <!-- Folder -->
  <div class="piece piece--blue folder" style="left:650px;top:50px;width:300px;height:560px;">
    <div class="faint-block" style="left:40px;top:300px;width:120px;height:120px;"></div>
    <div class="faint-block" style="left:180px;top:240px;width:40px;height:260px;"></div>
    <div class="lockup lockup--light" style="left:40px;top:90px;width:160px;font-size:11px;"><span class="lockup__mark" style="width:11px;height:11px;"></span>Summit Vale Management Corporation</div>
  </div>

  <!-- Letterhead -->
  <div class="piece piece--white letterhead" style="left:780px;top:90px;width:380px;height:540px;">
    <div class="lockup" style="left:24px;top:28px;width:150px;font-size:9px;"><span class="lockup__mark" style="width:10px;height:10px;"></span>Summit Vale Management Corporation</div>
    <div style="position:absolute;left:200px;top:26px;font-size:6.5px;line-height:1.7;color:var(--ink);">18 Harbor Lane, Suite 300<br>Easton, MA 02375<br>555-014-2200<br>03 5550 1188<br>info@summitvale.com<br>www.summitvalemgmt.com</div>
    <div class="faint-block" style="left:24px;top:360px;width:100px;height:90px;"></div>
    <svg class="wave" viewBox="0 0 380 120" height="120" preserveAspectRatio="none" aria-hidden="true">
      <path d="M0 80 C110 40 240 110 380 30 L380 120 L0 120 Z" fill="var(--bright)"/>
      <path d="M0 92 C120 56 250 120 380 44" fill="none" stroke="#fff" stroke-width="3"/>
      <path d="M0 100 C130 70 260 124 380 58 L380 120 L0 120 Z" fill="var(--navy)"/>
    </svg>
    <p class="footer-text" style="right:18px;bottom:12px;">SUMMIT VALE MANAGEMENT CORPORATION<br>ABN : 12 345 678 901</p>
  </div>

  <!-- Mailing label -->
  <div class="piece piece--white label" style="left:780px;top:690px;width:380px;height:160px;">
    <div class="lockup" style="left:18px;top:18px;width:150px;font-size:8px;"><span class="lockup__mark" style="width:9px;height:9px;"></span>Summit Vale Management Corporation</div>
    <div style="position:absolute;left:170px;top:22px;font-size:7px;color:var(--ink);">18 Harbor Lane, Suite 300 Easton, MA 02375</div>
    <div class="faint-block" style="left:18px;top:70px;width:70px;height:64px;"></div>
    <div class="label__band" style="height:10px;"></div>
  </div>
</section>

<!-- Business cards, large -->
<section class="band band--cards">
  <div class="piece piece--blue card-front" style="left:600px;top:100px;width:520px;height:300px;">
    <div class="faint-block" style="left:60px;top:150px;width:120px;height:120px;"></div>
    <div class="faint-block" style="left:360px;top:60px;width:50px;height:240px;"></div>
    <div class="lockup lockup--light" style="left:110px;top:120px;width:320px;font-size:20px;justify-content:center;"><span class="lockup__mark" style="width:18px;height:18px;"></span>Summit Vale Management Corporation</div>
  </div>

  <div class="piece piece--white card-back" style="left:110px;top:340px;width:600px;height:340px;">
    <div class="person__name" style="left:36px;top:28px;font-size:28px;">Alan Porter</div>
    <div class="person__role" style="left:100px;top:66px;font-size:18px;">Manager</div>
    <div class="lockup" style="left:360px;top:50px;width:210px;font-size:14px;"><span class="lockup__mark" style="width:16px;height:16px;"></span>Summit Vale Management Corporation</div>
    <ul class="contact-list" style="left:36px;top:118px;font-size:15px;line-height:1.45;">
      <li><svg width="12" height="14" viewBox="0 0 12 16" aria-hidden="true"><path d="M6 0a6 6 0 0 0-6 6c0 4.5 6 10 6 10s6-5.5 6-10a6 6 0 0 0-6-6zm0 8.5A2.5 2.5 0 1 1 6 3.5a2.5 2.5 0 0 1 0 5z"/></svg>18 Harbor Lane, Suite 300</li>
      <li style="padding-left:20px;">Easton, MA 02375</li>
      <li><svg width="12" height="12" viewBox="0 0 16 16" aria-hidden="true"><path d="M3.6 0.8l2.3 2.9-1.4 2a9.5 9.5 0 0 0 5.8 5.8l2-1.4 2.9 2.3-1.7 2.8C7.8 15 1 8.2 0.8 2.5z"/></svg>555-014-2200</li>
      <li><svg width="12" height="12" viewBox="0 0 16 16" aria-hidden="true"><path d="M3.6 0.8l2.3 2.9-1.4 2a9.5 9.5 0 0 0 5.8 5.8l2-1.4 2.9 2.3-1.7 2.8C7.8 15 1 8.2 0.8 2.5z"/></svg>03 5550 1188</li>
      <li><svg width="12" height="10" viewBox="0 0 16 12" aria-hidden="true"><path d="M0 0h16v12H0zm1.5 1.5L8 6.5l6.5-5z" fill-rule="evenodd"/></svg>info@summitvale.com</li>
      <li><svg width="12" height="12" viewBox="0 0 16 16" aria-hidden="true"><circle cx="8" cy="8" r="7" fill="none" stroke="var(--ink)" stroke-width="1.6"/><path d="M1 8h14M8 1v14" stroke="var(--ink)" stroke-width="1.4"/></svg>www.summitvalemgmt.com</li>
    </ul>
    <svg class="wave" viewBox="0 0 600 110" height="110" preserveAspectRatio="none" aria-hidden="true">
      <path d="M0 50 C170 20 380 80 600 14 L600 110 L0 110 Z" fill="var(--bright)"/>
      <path d="M0 62 C180 34 390 92 600 28" fill="none" stroke="#fff" stroke-width="3"/>
      <path d="M0 74 C190 50 400 102 600 42 L600 110 L0 110 Z" fill="var(--royal)"/>
    </svg>
    <p class="footer-text" style="right:28px;bottom:18px;font-size:10px;text-align:left;">SUMMIT VALE MANAGEMENT CORPORATION<br>ABN : 12 345 678 901</p>
  </div>
</section>

<!-- Mailing label, large -->
<section class="band band--label">
  <div class="piece piece--white label" style="left:30px;top:280px;width:540px;height:270px;">
    <div class="lockup" style="left:20px;top:24px;width:200px;font-size:11px;"><span class="lockup__mark" style="width:12px;height:12px;"></span>Summit Vale Management Corporation</div>
    <div style="position:absolute;left:240px;top:42px;font-size:10px;color:var(--royal);">18 Harbor Lane, Suite 300 Easton, MA 02375</div>
    <div class="label__line" style="left:20px;top:62px;width:500px;"></div>
    <div class="faint-block" style="left:20px;top:120px;width:110px;height:110px;"></div>
    <div class="label__band" style="height:14px;"></div>
  </div>
</section>

<!-- Notebook cover -->
<section class="band band--notebook">
  <div class="piece piece--blue notebook" style="left:80px;top:80px;width:460px;height:640px;border-radius:14px;overflow:visible;background:var(--navy);">
    <div class="spiral" aria-hidden="true">
      <span></span><span></span><span></span><span></span><span></span><span></span><span></span><span></span><span></span><span></span><span></span><span></span><span></span><span></span><span></span><span></span><span></span><span></span><span></span>
    </div>
    <div class="faint-block" style="left:60px;top:380px;width:140px;height:140px;"></div>
    <div class="faint-block" style="left:260px;top:300px;width:50px;height:340px;"></div>
    <div class="faint-block" style="left:340px;top:360px;width:40px;height:280px;"></div>
    <div class="lockup lockup--light" style="left:90px;top:90px;width:300px;font-size:15px;justify-content:center;text-align:center;"><span class="lockup__mark" style="width:14px;height:14px;"></span>Summit Vale Management Corporation</div>
  </div>
</section>

</body>
</html>
```